Sudden Tides "Lantern Road" New Single Cover

Create cover artwork for the band Sudden Tides' new single "Lantern Road" being released early 2020. Style, font and graphics to be consistent with band's previous releases and overall brand identity. Visit www.suddentidesband.example and our Spotify page https://music.example.net/artist/7QzWpLx3RtVnKd8e2YbHcJ?si=MUrTgKa4PLe7skvWq2AmZd to view our previous releases and overall brand identity. Some examples attached as well. We are looking for someone to work with on future projects as well.

Lyrics are here: https://docs.example.org/document/d/3KTp9wrn_2ZQa8eXb4Lo_fimH7C5m83Jz4Pd70hrtVcA/edit

Music is here: https://audiostream.example.com/suddentides/lantern-road/s-pzkwa

Font styles to use
Sans Serif

Colors

Designer to choose colors to be used in the design.

Requirements
Must have
• Must be consistent with current brand identity and with prior album / single art.

```html
<!DOCTYPE html>
<html lang="en">
<head>
<meta charset="utf-8">
<title>Sudden Tides – Lantern Road</title>
<link rel="stylesheet" href="https://fonts.googleapis.com/css2?family=Josefin+Sans:wght@200;300;400&family=Poiret+One&display=swap">
<style>
  :root {
    --navy: #1c2f57;
    --white: #ffffff;
    --teal: #26a9a6;
    --olive: #8fa85f;
    --amber: #f4ab2c;
  }
  html, body {
    margin: 0;
    padding: 0;
    width: 1200px;
    height: 1200px;
    overflow: hidden;
    background: var(--navy);
  }
  .cover {
    position: relative;
    width: 1200px;
    height: 1200px;
    background: var(--navy);
  }
  .cover__frame {
    position: absolute;
    left: 50px;
    top: 55px;
    width: 1096px;
    height: 1093px;
    border: 2px solid var(--white);
    box-sizing: border-box;
  }
  .cover__title {
    position: absolute;
    left: 0;
    top: 0;
    width: 1200px;
    height: 1200px;
  }
  .title-text {
    font-family: "Josefin Sans", sans-serif;
    font-weight: 200;
    font-size: 280px;
  }
  .band-name {
    position: absolute;
    left: 0;
    right: 0;
    top: 925px;
    margin: 0;
    text-align: center;
    font-family: "Josefin Sans", sans-serif;
    font-weight: 400;
    font-size: 62px;
    letter-spacing: 6px;
    color: var(--white);
    line-height: 1;
  }
  .members {
    position: absolute;
    left: 0;
    right: 0;
    top: 1050px;
    display: flex;
    justify-content: center;
    align-items: center;
    margin: 0;
    padding: 0;
    list-style: none;
    font-family: "Poiret One", sans-serif;
    font-size: 25px;
    color: var(--white);
    letter-spacing: 0.5px;
  }
  .members__item {
    padding: 2px 7px;
    line-height: 1.3;
  }
  .members__item + .members__item {
    border-left: 1.5px solid var(--white);
  }
</style>
</head>
<body>
  <main class="cover">
    <div class="cover__frame"></div>

    <svg class="cover__title" viewBox="0 0 1200 1200" aria-labelledby="single-title">
      <title id="single-title">Lantern Road</title>
      <defs>
        <linearGradient id="line-one-fill" gradientUnits="userSpaceOnUse" x1="0" y1="280" x2="0" y2="485">
          <stop offset="0" stop-color="var(--teal)"/>
          <stop offset="0.5" stop-color="var(--olive)"/>
          <stop offset="1" stop-color="var(--amber)"/>
        </linearGradient>
        <linearGradient id="line-two-fill" gradientUnits="userSpaceOnUse" x1="0" y1="565" x2="0" y2="770">
          <stop offset="0" stop-color="var(--teal)"/>
          <stop offset="0.5" stop-color="var(--olive)"/>
          <stop offset="1" stop-color="var(--amber)"/>
        </linearGradient>
      </defs>

      <text class="title-text" x="600" y="482" text-anchor="middle"
            textLength="970" lengthAdjust="spacingAndGlyphs"
            fill="url(#line-one-fill)">LANTERN</text>

      <g class="title-text" fill="url(#line-two-fill)" text-anchor="middle">
        <text x="244" y="767">R</text>
        <text x="468" y="767">O</text>
        <text x="713" y="767">A</text>
        <text x="940" y="767">D</text>
      </g>

      <circle class="title-burst" cx="468" cy="667" r="68" fill="var(--white)" fill-opacity="0.18"
              role="img" aria-label="Radiating white sunburst of fine lines set inside the letter O"/>
    </svg>

    <h1 class="band-name">SUDDEN TIDES</h1>

    <ul class="members">
      <li class="members__item">Mara Quillen</li>
      <li class="members__item">Tobias Renwick</li>
      <li class="members__item">Elise Harrow</li>
    </ul>
  </main>
</body>
</html>
```